Business Cards that are elegant and wow

I want to create and print business cards that represent my brand and stand out from the rest. We want to ensure they stay in our branding and the integrity is not lost. I am happy to look at different shapes like square etc.

It will be printed on very thick cards and will be stylish .

I want to create and print business cards that represent my brand and stand out from the rest. We want to ensure they stay in ur branding and the integrity is not lost. I am happy to look at different shapes like square etc.

Target Market(s)

real estate professionals

Industry/Entity Type

Real Estate

Contact Information for Business Card

Maren Holt
hello@brightfernrealty.com.au
brightfernrealty.com.au
0487 316 252 (SMS)

Colors

Designer to choose colors to be used in the design.

Requirements
Must have
• My logo
• email
• website
• Name
Nice to have
• I like the idea of printing with foil or spot gloss. You want it to stand out in a sea.
Should not have
• I would like you to stay in my colour themes. Don't change the colour of my logo

```html
<!DOCTYPE html>
<html lang="en">
<head>
<meta charset="utf-8">
<title>Bright Fern Realty — Business Card</title>
<link rel="stylesheet" href="https://fonts.googleapis.com/css2?family=Lato:wght@400;700&family=Montserrat:wght@500&display=swap">
<style>
  :root {
    --bg: #e9ecef;
    --card-white: #ffffff;
    --brand-blue: #00a3e0;
    --brand-blue-deep: #0088c8;
    --brand-pink: #e0137a;
    --mark-grey: #e6eef3;
  }
  * { margin: 0; padding: 0; box-sizing: border-box; }
  html, body { width: 1200px; height: 900px; overflow: hidden; }
  body {
    background: var(--bg);
    font-family: "Lato", sans-serif;
    display: flex;
    flex-direction: column;
    align-items: center;
    justify-content: center;
    gap: 44px;
  }
  .card {
    position: relative;
    width: 640px;
    height: 390px;
    border-radius: 22px;
    overflow: hidden;
    box-shadow: 0 10px 28px rgba(0,0,0,0.18);
  }
  /* Front */
  .card-front { background: var(--card-white); }
  .brand {
    position: absolute;
    top: 44px; left: 44px;
    display: flex; align-items: center; gap: 14px;
  }
  .brand-dot {
    width: 46px; height: 46px;
    border-radius: 50%;
    border: 3px solid var(--brand-pink);
  }
  .brand-name {
    font-family: "Montserrat", sans-serif;
    font-weight: 500;
    font-size: 30px;
    letter-spacing: 1px;
    color: var(--brand-pink);
    text-transform: uppercase;
    line-height: 1;
  }
  .divider {
    position: absolute;
    left: 44px; right: 44px; top: 170px;
    height: 2px;
    background: var(--brand-blue);
  }
  .holder {
    position: absolute;
    right: 44px; top: 100px;
    text-align: right;
  }
  .holder-name {
    font-size: 34px;
    font-weight: 400;
    letter-spacing: 2px;
    color: var(--brand-blue);
    text-transform: uppercase;
    line-height: 1;
  }
  .holder-role {
    margin-top: 6px;
    font-size: 17px;
    color: var(--brand-pink);
  }
  .contacts {
    position: absolute;
    left: 44px; top: 196px;
    list-style: none;
  }
  .contacts li {
    display: flex; align-items: center; gap: 10px;
    font-size: 17px;
    color: var(--brand-pink);
    line-height: 28px;
  }
  .contacts svg { width: 13px; height: 13px; fill: var(--brand-blue); flex: none; }
  .wave { position: absolute; left: 0; bottom: 0; width: 640px; height: 390px; }

  /* Back */
  .card-back {
    background: linear-gradient(135deg, var(--brand-blue) 0%, var(--brand-blue-deep) 100%);
    display: flex; align-items: center; justify-content: center; gap: 22px;
  }
  .card-back .brand-dot { width: 84px; height: 84px; border-color: var(--mark-grey); border-width: 4px; }
  .card-back .brand-name { color: var(--mark-grey); font-size: 44px; }
</style>
</head>
<body>

  <section class="card card-front">
    <div class="brand">
      <span class="brand-dot"></span>
      <span class="brand-name">Bright Fern Realty</span>
    </div>

    <div class="holder">
      <p class="holder-name">Maren Holt</p>
      <p class="holder-role">Director at Bright Fern Realty</p>
    </div>

    <div class="divider"></div>

    <ul class="contacts">
      <li>
        <svg viewBox="0 0 24 24"><path d="M6.6 10.8a15.1 15.1 0 0 0 6.6 6.6l2.2-2.2c.3-.3.7-.4 1-.2 1.1.4 2.3.6 3.6.6.6 0 1 .4 1 1V20c0 .6-.4 1-1 1A17 17 0 0 1 3 4c0-.6.4-1 1-1h3.5c.6 0 1 .4 1 1 0 1.3.2 2.5.6 3.6.1.3 0 .7-.2 1z"/></svg>
        0487 316 252 (SMS)
      </li>
      <li>
        <svg viewBox="0 0 24 24"><path d="M2 5h20v14H2zm2 2v.5l8 5 8-5V7zm0 2.8V17h16V9.8l-8 5z"/></svg>
        hello@brightfernrealty.com.au
      </li>
      <li>
        <svg viewBox="0 0 24 24"><circle cx="12" cy="12" r="10"/></svg>
        www.brightfernrealty.com.au
      </li>
    </ul>

    <svg class="wave" viewBox="0 0 640 390" aria-hidden="true">
      <path d="M0 300 C 160 330, 380 330, 520 390 L0 390 Z" fill="var(--brand-blue)"/>
      <path d="M0 292 C 160 322, 380 322, 530 390" fill="none" stroke="var(--brand-pink)" stroke-width="5"/>
    </svg>
  </section>

  <section class="card card-back">
    <span class="brand-dot"></span>
    <span class="brand-name">Bright Fern Realty</span>
  </section>

</body>
</html>
```